R J Penn Accounting & SMSF Auditing needs a Web Site Design

I need some examples of what a web design can look like for my business.
The business name is above and I have already registered a domain name of www.penn-smsf.com.au
I have attached my current letterhead and business cards and would like to maintain these colours basically Red on White with some black

```html
<!DOCTYPE html>
<html lang="en">
<head>
<meta charset="utf-8">
<title>R J Penn Accounting &amp; SMSF Auditing</title>
<link rel="stylesheet" href="https://fonts.googleapis.com/css2?family=Open+Sans:wght@400;600&family=Cabin:wght@400;600&display=swap">
<style>
:root{
  --red:#c8102e;
  --dark:#222326;
  --footer:#1e1f21;
  --tile:#3d3e41;
  --white:#ffffff;
  --ink:#2a2a2a;
  --panel:rgba(255,255,255,0.93);
}
*{margin:0;padding:0;box-sizing:border-box}
html,body{width:1200px;height:720px;overflow:hidden;background:var(--dark)}
body{font-family:"Open Sans",sans-serif;position:relative}
.site-header{position:absolute;left:0;top:0;width:1200px;height:77px;
  background:radial-gradient(ellipse 260px 70px at 220px 30px,#3a3b3f,var(--dark));
  border-bottom:2px solid var(--red)}
.brand{position:absolute;left:126px;top:26px;color:var(--white);font-size:19px;font-weight:400;letter-spacing:.3px}
.main-nav{position:absolute;top:31px;left:0;width:1200px;font-size:11.5px;letter-spacing:.6px}
.main-nav a{position:absolute;color:var(--white);text-decoration:none}
.main-nav a.active{color:var(--red)}
.hero{position:absolute;left:0;top:79px;width:1200px;height:542px;
  background:radial-gradient(ellipse 380px 200px at 700px 60px,#8a8a8a,transparent),
  linear-gradient(160deg,#9a9a9a 0%,#d4d4d4 35%,#bdbdbd 60%,#6e6e6e 100%)}
.portrait{position:absolute;left:190px;top:162px;width:163px;height:218px;
  background:linear-gradient(160deg,#3a2718,#7a5a3c 55%,#a58a6a);z-index:2}
.intro-panel{position:absolute;left:144px;top:339px;width:913px;height:202px;background:var(--panel)}
.intro-text{position:absolute;left:47px;top:56px;width:460px;font-family:"Cabin",sans-serif;
  font-size:14.6px;line-height:24px;color:var(--ink)}
.intro-text strong{font-weight:600}
.more-btn{position:absolute;left:203px;top:139px;width:123px;height:30px;background:var(--red);
  color:var(--white);font-family:"Cabin",sans-serif;font-size:12px;display:flex;align-items:center;justify-content:center;gap:7px}
.services{position:absolute;left:556px;top:16px;width:340px;height:170px;display:grid;
  grid-template-columns:1fr 1fr;grid-template-rows:1fr 1fr;gap:1px;background:#d8d8d8}
.service{background:var(--tile);color:var(--white);font-size:11.5px;display:flex;flex-direction:column;
  align-items:center;justify-content:center;gap:8px}
.service svg{width:26px;height:26px}
.slider-dots{position:absolute;left:560px;top:563px;display:flex;gap:9px}
.slider-dots span{width:13px;height:13px;border:1px solid var(--white)}
.slider-dots span.on{background:var(--white)}
.site-footer{position:absolute;left:0;top:621px;width:1200px;height:99px;background:var(--footer);
  color:var(--white);font-size:8.8px}
.copy{position:absolute;left:126px;top:36px}
.contact-line{position:absolute;left:126px;top:53px}
.contact-line em{font-style:normal;color:var(--red)}
.contact-line span{margin-right:7px}
.social{position:absolute;left:971px;top:36px;display:flex;gap:7px}
.social span{width:24px;height:24px;background:#4a4b4f}
</style>
</head>
<body>
<header class="site-header">
  <div class="brand">R J Penn Accounting &amp; SMSF Auditing</div>
  <nav class="main-nav">
    <a class="active" href="#" style="left:718px">HOME</a>
    <a href="#" style="left:798px">SERVICES</a>
    <a href="#" style="left:896px">ABOUT US</a>
    <a href="#" style="left:1001px">CONTACT</a>
  </nav>
</header>

<section class="hero" role="img" aria-label="Soft black and white photo of a desk with a cup, notebook and pen"></section>
<div class="portrait" role="img" aria-label="Portrait photo of the principal accountant"></div>

<section class="intro-panel">
  <p class="intro-text"><strong>Robert J. Penn</strong> is the leading provider of innovative information and delivers collaborative solutions for our people and partners to effectively assist them in achieving their objectives.</p>
  <a class="more-btn">MORE INFO
    <svg width="16" height="16" viewBox="0 0 16 16"><circle cx="8" cy="8" r="7" fill="none" stroke="#fff" stroke-width="1.6"/><path d="M4.5 8h6M8 5.2 10.8 8 8 10.8" fill="none" stroke="#fff" stroke-width="1.6"/></svg>
  </a>
  <div class="services">
    <div class="service">
      <svg viewBox="0 0 26 26"><rect x="1" y="1" width="11" height="11" fill="#c8102e"/><rect x="14" y="1" width="11" height="11" fill="#c8102e"/><rect x="1" y="14" width="11" height="11" fill="#c8102e"/><rect x="14" y="14" width="11" height="11" fill="#c8102e"/></svg>
      ACCOUNTING</div>
    <div class="service">
      <svg viewBox="0 0 26 26"><rect x="6" y="1" width="17" height="24" fill="#c8102e"/><path d="M3 5h6M3 10h6M3 15h6M3 20h6" stroke="#c8102e" stroke-width="2"/><rect x="17" y="3" width="2" height="20" fill="#3d3e41"/></svg>
      AUDITING</div>
    <div class="service">
      <svg viewBox="0 0 26 26"><rect x="5" y="9" width="20" height="12" fill="none" stroke="#c8102e" stroke-width="1.6"/><path d="M12 14h10M12 17h10M1 5l11 9" stroke="#c8102e" stroke-width="2"/></svg>
      PAYROLL</div>
    <div class="service">
      <svg viewBox="0 0 26 26"><path d="M9 6V3h8v3" fill="none" stroke="#c8102e" stroke-width="2"/><rect x="1" y="7" width="24" height="17" rx="2" fill="#c8102e"/><path d="M7 7v17M19 7v17" stroke="#3d3e41" stroke-width="1.2"/></svg>
      MANAGEMENT REPORTING</div>
  </div>
</section>

<div class="slider-dots"><span></span><span class="on"></span><span></span><span></span></div>

<footer class="site-footer">
  <p class="copy">COPYRIGHT © 2014 &nbsp;PENN-SMSF.COM.AU &nbsp;ALL RIGHTS RESERVED</p>
  <p class="contact-line"><span><em>OFFICE:</em> PO BOX 118 RIVERVALE WA 6103</span> <span><em>MOBILE:</em> 0400 555 018</span> <span><em>EMAIL:</em> ROBERTPENN@PENN-SMSF.COM.AU</span></p>
  <div class="social"><span></span><span></span><span></span></div>
</footer>
</body>
</html>
```